Kelvora trustee touch - styling

We have a prototyped single page application. The content is in place what we need is restyling to

- make it more user friendly
- modern look and feel
- improve accessibility features
- use our brand guidelines (screen shots attached of the full website)

Prototype is available at http://plinthdesk.examplehost.net/

Target form factor:
Primary - tablet
Secondary - desktop

Target Market(s)

Business users - not financial professionals but people working for big companies who have some limited training in the concepts

Number of Pages Required

1 page

Requirements
Must have
• Touch user interface

```html
<!DOCTYPE html>
<html lang="en">
<head>
<meta charset="utf-8">
<title>Kelvora – Flight Plan</title>
<link rel="stylesheet" href="https://fonts.googleapis.com/css2?family=Arimo:wght@400;700&display=swap">
<style>
:root{
  --brand-blue:#0a5fb0;
  --accent-blue:#4aa8e6;
  --magenta:#a51164;
  --page-bg:#f3f3f3;
  --card-bg:#ffffff;
  --chart-bg:#fafafa;
  --grid:#e2e2e2;
  --text:#222222;
  --muted:#555555;
  --red:#d0021b;
}
*{box-sizing:border-box;margin:0;padding:0}
html,body{width:1200px;height:939px;overflow:hidden}
body{background:var(--page-bg);font-family:"Arimo",Arial,sans-serif;color:var(--text);position:relative}
.site-header{position:absolute;left:0;top:0;width:1200px;height:96px;background:var(--brand-blue)}
.brand{position:absolute;left:100px;top:28px;color:#fff;font-size:34px;font-weight:700;letter-spacing:-1px}
.context-nav span{position:absolute;top:42px;color:#fff;font-size:14px}
.lock-tab{position:absolute;left:64px;top:167px;width:46px;height:42px;background:var(--accent-blue)}
.lock-tab svg{position:absolute;left:13px;top:9px}
.panel{position:absolute;left:110px;top:123px;width:980px;height:722px;background:var(--card-bg)}
.tabs{position:absolute;left:0;top:0;width:980px;height:86px;border-bottom:2px solid var(--magenta)}
.tab{position:absolute;top:0;height:84px;text-align:center}
.tab-title{display:block;margin-top:28px;font-size:14px;color:var(--text)}
.tab-metric{display:block;margin-top:14px;font-size:12px;color:var(--brand-blue)}
.tab-metric b{font-size:13px}
.tab-metric .down{color:var(--red)}
.tab.active{background:var(--magenta)}
.tab.active .tab-title,.tab.active .tab-metric{color:#fff}
.chart{position:absolute;left:29px;top:146px;width:920px;height:439px;background:var(--chart-bg)}
.controls{position:absolute;left:0;top:618px;width:980px;height:104px;border-top:1px solid #ececec}
.controls .divider{position:absolute;left:515px;top:0;width:1px;height:104px;background:#ececec}
.control-label{position:absolute;top:32px;font-size:14px;font-weight:700;color:var(--muted)}
.track{position:absolute;top:31px;height:14px;border-radius:7px;background:#f0f0f0;border:1px solid #e0e0e0}
.knob{position:absolute;width:18px;height:18px;border-radius:50%;top:29px}
.knob.magenta{background:var(--magenta);border:2px solid #6d0b42}
.knob.blue{background:var(--accent-blue);border:2px solid #1f6aa3}
.scale{position:absolute;top:59px;font-size:14px;color:var(--muted)}
.scale.value{font-weight:700}
.site-footer{position:absolute;left:0;top:870px;width:1200px;height:69px;border-bottom:1px solid #ddd}
.copyright{position:absolute;left:111px;top:18px;font-size:14px;font-weight:700;color:var(--muted)}
.social{position:absolute;top:17px;width:21px;height:21px;border-radius:50%;background:var(--brand-blue)}
.page-code{position:absolute;left:1147px;top:21px;font-size:14px;color:#777}
</style>
</head>
<body>
<header class="site-header">
  <div class="brand">Kelvora</div>
  <nav class="context-nav">
    <span style="left:553px">XYZ Limited</span>
    <span style="left:676px">XYZ Pension Scheme</span>
    <span style="left:851px">Technical Provisions</span>
    <span style="left:1015px">October 2014</span>
  </nav>
</header>

<div class="lock-tab" aria-label="Locked">
  <svg width="20" height="24" viewBox="0 0 20 24"><path d="M5 10V7a5 5 0 0 1 10 0v3" fill="none" stroke="#fff" stroke-width="2.5"/><rect x="2" y="10" width="16" height="12" rx="1" fill="#fff"/><rect x="9" y="14" width="2" height="4" fill="#4aa8e6"/></svg>
</div>

<main class="panel">
  <div class="tabs">
    <div class="tab" style="left:0;width:218px"><span class="tab-title">Daily Valuations</span><span class="tab-metric"><b>91%</b> Funding Level</span></div>
    <div class="tab" style="left:218px;width:211px"><span class="tab-title">Funding level changes</span><span class="tab-metric"><b class="down">-1.7 % ▾</b> Funding Level Change</span></div>
    <div class="tab active" style="left:429px;width:205px"><span class="tab-title">Flight Plan</span><span class="tab-metric"><b>3% ▾</b> Progress Against flight plan</span></div>
    <div class="tab" style="left:634px;width:346px"><span class="tab-title">ALM</span><span class="tab-metric"><b>67 %</b> 10 Years Protected Funding Level</span></div>
  </div>

  <svg class="chart" width="920" height="439" viewBox="139 269 920 439" font-family="Arimo, Arial, sans-serif" font-size="12" role="img" aria-label="Funding level against flight plan">
    <g stroke="var(--grid)" stroke-width="1">
      <line x1="208" x2="1026" y1="328" y2="328"/><line x1="208" x2="1026" y1="383" y2="383"/>
      <line x1="208" x2="1026" y1="438" y2="438"/><line x1="208" x2="1026" y1="493" y2="493"/>
      <line x1="208" x2="1026" y1="548" y2="548"/><line x1="208" x2="1026" y1="603" y2="603"/>
      <line x1="208" x2="1026" y1="658" y2="658" stroke="#ccc"/>
      <line x1="208" x2="208" y1="282" y2="658" stroke="#ccc"/>
    </g>
    <g stroke="#ccc"><line x1="248" x2="248" y1="658" y2="665"/><line x1="354" x2="354" y1="658" y2="665"/><line x1="459" x2="459" y1="658" y2="665"/><line x1="565" x2="565" y1="658" y2="665"/><line x1="670" x2="670" y1="658" y2="665"/><line x1="775" x2="775" y1="658" y2="665"/><line x1="880" x2="880" y1="658" y2="665"/></g>
    <g fill="#333" text-anchor="end">
      <text x="198" y="333">100%</text><text x="198" y="388">95%</text><text x="198" y="443">90%</text>
      <text x="198" y="498">85%</text><text x="198" y="553">80%</text><text x="198" y="608">75%</text><text x="198" y="663">70%</text>
    </g>
    <g fill="#111" text-anchor="middle">
      <text x="251" y="694">29 / Nov / 2013</text><text x="353" y="694">29 / Nov / 2013</text>
      <text x="457" y="694">29 / Nov / 2013</text><text x="569" y="694">30 / Dec / 2013</text>
      <text x="670" y="694">2014</text><text x="776" y="694">2015</text><text x="881" y="694">2016</text>
    </g>
    <polyline fill="none" stroke="var(--accent-blue)" stroke-width="1" points="220,382 258,373 272,381 289,370 311,378 331,370 344,377 363,373 391,386 416,386 439,400 480,388 503,394 537,376 547,383 565,375 592,376 604,370 621,375 629,375 646,390 1024,537"/>
    <line x1="422" y1="371" x2="1016" y2="520" stroke="var(--magenta)" stroke-width="2"/>
    <circle cx="439" cy="400" r="5" fill="var(--accent-blue)"/>
    <path d="M433 307H529V375H452L441 391L440 375H433Z" fill="#efefef" stroke="#ddd"/>
    <text x="440" y="340" fill="var(--magenta)" font-size="14">29/Nov/2013</text>
    <text x="443" y="358" fill="#222" font-size="14">90.80 %</text>
  </svg>

  <section class="controls">
    <div class="divider"></div>
    <span class="control-label" style="left:32px">Investment Strategy</span>
    <div class="track" style="left:190px;width:287px"></div>
    <div class="knob magenta" style="left:182px"></div>
    <span class="scale" style="left:162px">Matching</span>
    <span class="scale value" style="left:298px">100% / 0%</span>
    <span class="scale" style="left:447px">Growth</span>

    <span class="control-label" style="left:539px">Contributions</span>
    <div class="track" style="left:668px;width:282px"></div>
    <div class="knob blue" style="left:659px"></div>
    <span class="scale" style="left:654px">£0m</span>
    <span class="scale value" style="left:790px">£0.0m</span>
    <span class="scale" style="left:929px">£30m</span>
  </section>
</main>

<footer class="site-footer">
  <span class="copyright">© 2014 Compnay Name ,All Rights Reserved</span>
  <span class="social" style="left:1017px" aria-label="Social link"></span>
  <span class="social" style="left:1043px" aria-label="Social link"></span>
  <span class="social" style="left:1068px" aria-label="Social link"></span>
  <span class="page-code">C5</span>
</footer>
</body>
</html>
```